Business Flyer for Wedding BBQ Caterer

Need a new 2-sided 3.75 (wide) x 8.25 (high) flyer for my BBQ business called Hearthside Hog. We mainly cater rustic barn weddings in the DFW (Dallas/Fort Worth) area. This flyer will be given to the wedding venues that we cater in for them to hand out to the brides that book with them.

FRONT:
- Rustic look, whites and wedding friendly. Appealing to brides. No red, white & blue on this brochure. I like this distressed white wooden background.
https://lumovale.files.example.com/2013/05/stockframe_7314058-white-wood-texture-background.jpg

- PHOTOS SELL. Large pic (top_photo.jpg) on the front at the top to capture attention.

- The Vow Finest of Nuptials award image. (blue circle)

- Smaller Hearthside Hog logo and a little faded too so that it's not as bright red and blue. I also included a branded version of it that looks like it's burnt into the wood.

- Paragraph about who we are. (Wedding brochure content.docx)

- Social media handles and contact info in a footer on the front.
Instagram @hearthsidehogweddings
Facebook @hearthsidehog
Website www.hearthsidehog.example
info@hearthsidehog.example
555-304-7182
--------------------------------------------------------------------------------------------------------------
BACK:
- TOP - 2-3 of the food images.

- MIDDLE - Say somewhere that our prices range from $10-$15 per guest.

- BOTTOM - Short version of our menu (no descriptions). (See the Word doc in the brief)

Target Market(s)

Wedding venues, brides and grooms

Industry/Entity Type

Catering

Colors

Designer to choose colors to be used in the design.

Requirements
Must have
• Largest pics possible on the front
• Rustic look
• Whites
• No red, white & blue
• Elegant look.

```html
<!DOCTYPE html>
<html lang="en">
<head>
<meta charset="utf-8">
<title>Hearthside Hog – Wedding Flyer</title>
<link rel="stylesheet" href="https://fonts.googleapis.com/css2?family=Libre+Baskerville:wght@400;700&family=Montserrat:wght@400;600&display=swap">
<style>
  :root {
    --stage: #9c9c9c;
    --paper: #f4f4f3;
    --paper-shade: #e6e6e4;
    --accent: #8a4b2a;
    --accent-soft: #a9825f;
    --sage: #5e7355;
    --ink: #2e2e2e;
    --ink-soft: #4a4a4a;
    --badge: #d9c7ad;
    --rule: #7a5437;
  }
  * { box-sizing: border-box; margin: 0; padding: 0; }
  html, body { width: 1200px; height: 1200px; overflow: hidden; }
  body { background: var(--stage); font-family: "Montserrat", sans-serif; color: var(--ink); position: relative; }

  .panel {
    position: absolute; top: 127px; width: 460px; height: 1013px; overflow: hidden;
    background:
      repeating-linear-gradient(90deg, rgba(0,0,0,0.018) 0 2px, transparent 2px 9px, rgba(0,0,0,0.012) 9px 10px, transparent 10px 23px),
      linear-gradient(180deg, var(--paper) 0%, #fbfbfa 50%, var(--paper-shade) 100%);
    box-shadow: 0 3px 14px rgba(0,0,0,0.35);
  }
  .panel--front { left: 109px; }
  .panel--back { left: 646px; }
  .abs { position: absolute; }

  .photo { position: absolute; border: 3px solid #fff; box-shadow: 0 2px 6px rgba(0,0,0,0.35); }

  /* Front */
  .hero-photo { left: 15px; top: 0; width: 445px; height: 370px; border: none; box-shadow: none;
    background: linear-gradient(160deg, #d9d4cc 0%, #b58b58 45%, #6d5033 70%, #ece9e4 100%); }
  .floral { left: 0; top: 0; width: 210px; height: 135px;
    background: radial-gradient(ellipse at 40% 40%, #d98fb0 0%, #e9b9cf 45%, rgba(240,220,230,0) 75%); }
  .tacos-photo { left: 31px; top: 373px; width: 248px; height: 186px;
    background: linear-gradient(90deg, #6a3f22 0%, #a8774c 30%, #efe8dd 50%, #8a5b36 75%, #5a3620 100%); }
  .pie-photo { left: 290px; top: 402px; width: 152px; height: 157px;
    background: radial-gradient(circle at 50% 60%, #3c2a33 0%, #6a4a52 40%, #c89a6c 60%, #d8d2cc 80%); }
  .brand-mark { left: 61px; top: 521px; width: 120px; height: 120px; border-radius: 50%; background: #e4e3e0; border: 2px solid #cfcdc8; }
  .brand-name { left: 41px; top: 646px; width: 160px; text-align: center; font-family: "Libre Baskerville", serif; font-weight: 700; font-size: 15px; color: #8a8a88; }
  .award-badge { left: 27px; top: 685px; width: 176px; height: 176px; border-radius: 50%; background: var(--badge); border: 4px solid #fff; box-shadow: 0 2px 6px rgba(0,0,0,0.25); }

  .intro-title { left: 228px; top: 583px; width: 220px; font-family: "Libre Baskerville", serif; font-weight: 700; font-size: 18px; color: var(--accent); white-space: nowrap; }
  .intro-title .stars { color: var(--ink); font-size: 11px; vertical-align: 3px; }
  .intro-copy { left: 228px; top: 613px; width: 212px; font-size: 12.8px; line-height: 16.5px; color: var(--ink-soft); text-align: justify; }

  .flower-pail { left: 330px; top: 850px; width: 112px; height: 118px;
    background: linear-gradient(180deg, #f6f6f2 0%, #dfe5d6 40%, #a9adb1 60%, #7d8287 100%); border-radius: 40% 40% 6px 6px; }

  .contact { left: 18px; width: 250px; font-family: "Libre Baskerville", serif; font-size: 11.5px; color: var(--ink); display: flex; align-items: center; gap: 10px; }
  .contact svg { width: 12px; height: 12px; flex: none; }
  .contact span { background: rgba(255,255,255,0.85); padding: 2px 5px; }
  .contact--phone { top: 885px; }
  .contact--web { top: 912px; }
  .contact--mail { top: 940px; }
  .social { left: 13px; top: 978px; font-family: "Libre Baskerville", serif; font-size: 11px; color: var(--ink); display: flex; gap: 10px; white-space: nowrap; }
  .social i { display: inline-block; width: 12px; height: 12px; border: 1.2px solid var(--accent-soft); border-radius: 50%; vertical-align: -2px; margin-right: 4px; }

  /* Back */
  .menu-title { left: 0; top: 14px; width: 460px; text-align: center; font-family: "Libre Baskerville", serif; font-weight: 700; font-size: 17px; color: var(--accent); }
  .price-line { left: 0; top: 33px; width: 460px; text-align: center; font-size: 16px; color: var(--ink); }
  .price-line b { color: var(--sage); font-weight: 600; }
  .section-title { font-family: "Libre Baskerville", serif; font-weight: 700; font-size: 17px; color: var(--accent); }
  .copy { font-size: 11.4px; line-height: 14.4px; color: var(--ink); text-align: justify; }
  .copy p + p { margin-top: 4.8px; }
  .item { color: var(--sage); font-weight: 600; }

  .sliders-photo { left: 14px; top: 93px; width: 164px; height: 144px;
    background: linear-gradient(90deg, #6b4225 0%, #a47040 35%, #f0e6d4 50%, #a47040 65%, #5c381e 100%); }
  .meat-photo { left: 14px; top: 405px; width: 162px; height: 124px;
    background: linear-gradient(135deg, #2b2523 0%, #c86a3e 35%, #e48b58 55%, #b5532e 75%, #3a302c 100%); }
  .dessert-photo { left: 14px; top: 743px; width: 162px; height: 146px;
    background: radial-gradient(circle at 60% 55%, #f2ead5 0%, #e4c98f 30%, #6a4128 65%, #3d261a 100%); }

  .bottom-rule { left: 0; bottom: 0; width: 460px; height: 6px; background: var(--rule); }
</style>
</head>
<body>

<section class="panel panel--front" aria-label="Flyer front">
  <div class="photo hero-photo" role="img" aria-label="Rustic buffet display with wooden crates, chafer, cast-iron pots and a burnt-end sign"></div>
  <div class="abs floral" role="img" aria-label="Watercolour pink roses and foliage"></div>
  <div class="photo tacos-photo" role="img" aria-label="Row of mini brisket tacos on a wooden board"></div>
  <div class="photo pie-photo" role="img" aria-label="Berry pie with a lattice crust"></div>

  <div class="abs brand-mark" aria-hidden="true"></div>
  <div class="abs brand-name">Hearthside Hog</div>
  <div class="abs award-badge" role="img" aria-label="Wedding listing award badge"></div>

  <h1 class="abs intro-title"><span class="stars">★★</span> Hearthside Hog <span class="stars">★★</span></h1>
  <p class="abs intro-copy">Where Rustic meets Elegance. Farmhouse meets Romantic. Hearthside Hog provides a timeless and classic backdrop for every element of the dining experience. From the reclaimed barnwood chafers all the way down to the mason-jar salt-n-pepper shakers, we strive to WOW your guests with some of the best premium meats in Texas presented in a stunning display that's rooted in unmistakable Lonestar Pride.</p>

  <div class="abs flower-pail" role="img" aria-label="Baby's breath bouquet in a galvanized tin pail"></div>

  <div class="abs contact contact--phone">
    <svg viewBox="0 0 12 12"><path d="M2.5 1 L4.5 1 L5 3.5 L3.8 4.4 Q5 7 7.6 8.2 L8.5 7 L11 7.5 L11 9.5 Q10.5 11 9 11 Q1 9.5 1 2.5 Q1 1 2.5 1Z" fill="var(--accent)"/></svg>
    <span>555-304-7182</span>
  </div>
  <div class="abs contact contact--web">
    <svg viewBox="0 0 12 12"><circle cx="6" cy="6" r="5" fill="none" stroke="var(--accent)" stroke-width="1.3"/><path d="M1 6 H11 M6 1 Q3 6 6 11 Q9 6 6 1" fill="none" stroke="var(--accent)" stroke-width="1"/></svg>
    <span>www.hearthsidehog.example</span>
  </div>
  <div class="abs contact contact--mail">
    <svg viewBox="0 0 12 12"><rect x="1" y="2.5" width="10" height="7" fill="var(--accent)"/><path d="M1 2.5 L6 6.5 L11 2.5" fill="none" stroke="#fff" stroke-width="1"/></svg>
    <span>info@hearthsidehog.example</span>
  </div>
  <div class="abs social">
    <span><i></i>Facebook @hearthsidehog</span>
    <span><i></i>Instagram @ hearthsidehog.example</span>
  </div>
</section>

<section class="panel panel--back" aria-label="Flyer back">
  <h2 class="abs menu-title">MENU</h2>
  <p class="abs price-line">prices range from <b>$10-$15</b> per guest</p>

  <h3 class="abs section-title" style="left:14px;top:66px;">APPETIZERS</h3>
  <div class="photo sliders-photo" role="img" aria-label="Tray of combo sliders"></div>
  <div class="abs copy" style="left:202px;top:101px;width:246px;">
    <p><span class="item">Combo Sliders</span> - Brisket &amp; pulled pork sliders served with all three of our BBQ sauces on the side.</p>
    <p><span class="item">Bacon Bombs</span> - Bacon-wrapped jalapenos filled with sausage and cheesy goodness smoked to perfection. Smoked Chicken Legs - Slow-smoked and tossed in one of our three BBQ sauces (sweet, tangy or spicy).</p>
  </div>
  <div class="abs copy" style="left:15px;top:263px;width:135px;"><p><span class="item">Texas Tater Skins</span> - Crispy potato skins topped with pulled pork, cheese &amp; BBQ sauce drizzled on top.</p></div>
  <div class="abs copy" style="left:163px;top:263px;width:145px;"><p><span class="item">Pimiento Cheese &amp; Sausage</span> - Made-from-scratch creamy pimiento cheese (aka The Caviar of the South) served with smoked sausage and a variety of crackers.</p></div>
  <div class="abs copy" style="left:325px;top:263px;width:123px;"><p><span class="item">Mini Brisket Tacos</span> - Smoked brisket wrapped in a mini corn tortilla topped with pico, cheese and guac on the side.</p></div>

  <h3 class="abs section-title" style="left:14px;top:376px;">MEATS</h3>
  <div class="photo meat-photo" role="img" aria-label="Smoked meats on the grill"></div>
  <div class="abs copy" style="left:202px;top:402px;width:246px;">
    <p><span class="item">Brisket</span> - This ain't big-chain brisket. It's premium Wagyu or Angus beef smoked slow-n-low for 12+ hours.</p>
    <p><span class="item">Sausage</span> Choose from cracked black pepper, jalapeno cheddar and more.</p>
    <p><span class="item">Turkey (NEW)</span> - You've got to try our new premium Apple-Rubbed Smoked Turkey Breast.</p>
    <p><span class="item">Ham</span> - Baked hams ain't got nothin on this smoked gem. We top it with a sweet, pineapple glaze.</p>
  </div>
  <div class="abs copy" style="left:19px;top:591px;width:131px;"><p><span class="item">Pork Ribs</span> - “Give me liberty or give me ribs.” Or something like that. Our St Louis ribs are fall off the bone good.</p></div>
  <div class="abs copy" style="left:162px;top:591px;width:133px;"><p><span class="item">Chicken</span> - I like pig butts and I cannot lie. We can barely pull it off the smoker without it falling !</p></div>
  <div class="abs copy" style="left:322px;top:591px;width:126px;"><p><span class="item">Pulled Pork</span> - I like pig butts and I cannot lie. We can barely pull it off the smoker without it falling</p></div>

  <h3 class="abs section-title" style="left:15px;top:699px;">DESSERT BAR</h3>
  <div class="photo dessert-photo" role="img" aria-label="Dessert table with mini pies and a wedding cake"></div>
  <div class="abs copy" style="left:205px;top:697px;width:243px;">
    <p><span class="item">Wedding Cakes</span> - Buttercream &amp; Fondant available with a dozen different flavors &amp; fillings.</p>
    <p><span class="item">Pies (Mini &amp; Whole)s</span> -American (Blueberry/Cherry), Pecan, Apple, Cherry, Buttermilk Chess, Lemon Chess, Key Lime, Coconut Cream, Banana Cream, Sugar-free Pecan, Chocolate Chess, Pumpkin (seasonal), Sweet Potato, Red Velvet, Sugar-free Apple.</p>
    <p style="margin-top:9px;"><span class="item">Cookies</span> - Chocolate Chip, Oatmeal Raisin, Pecan, Sugar, Snickerdoodle, Peanut Butter, White Chocolate Chip Macadamia.</p>
  </div>
  <div class="abs copy" style="left:13px;top:925px;width:135px;"><p><span class="item">Sweet Shots</span> - Peach Cobbler, Banana Pudding, Strawberry Shortcake, Key Lime, Chocolate Mousse.</p></div>
  <div class="abs copy" style="left:162px;top:925px;width:144px;"><p><span class="item">Mini Cheesecakes</span> - White Chocolate, Strawberry, Plain, Zebra (Cookies &amp; Cream), Turtle, Red Velvet.</p></div>
  <div class="abs copy" style="left:314px;top:925px;width:134px;"><p><span class="item">Bars &amp; Brownies</span> - Fudge Brownies, Brownies w/Pecans, Lemon Bars, Pecan Pie Bars</p></div>

  <div class="abs bottom-rule"></div>
</section>

</body>
</html>
```